* see below *
Project: Stationary for Law Firm
Stationary for Law Firm - Law
Stationary for Law Firm
Use standard fonts
Dorian Valesko, Esq.
Managing Partner
4382 Linden Terrace Brooklyn, New York 11356
dorian@valeskolegal.com
www.ValeskoLegal.com
This is a design for a stationary, not for a business card.
DorianValesko DorianValesko
This is a design for a stationary, not for a business card. I need a design for a letterhead stationary

```html
<!DOCTYPE html>
<html lang="en">
<head>
<meta charset="utf-8">
<title>Dorian Valesko, LLP — Stationery</title>
<link href="https://fonts.googleapis.com/css2?family=Cinzel:wght@500&family=Open+Sans:wght@400;600&display=swap" rel="stylesheet">
<style>
:root{
  --maroon:#8b2a34;
  --grey:#6b6c6f;
  --ink:#3a3a3c;
  --muted:#8a8a8d;
  --paper:#ffffff;
  --bg:#f3f3f4;
}
*{margin:0;padding:0;box-sizing:border-box}
html,body{width:1200px;height:936px;overflow:hidden;background:var(--bg)}
body{position:relative;font-family:"Open Sans",Arial,sans-serif;color:var(--ink)}
.sheet{position:absolute;background:var(--paper);box-shadow:0 2px 8px rgba(0,0,0,.12);overflow:hidden}
.brand{font-family:"Cinzel",Georgia,serif;font-weight:500;color:var(--maroon);letter-spacing:.04em;white-space:nowrap}
.mark{display:inline-block;background:var(--maroon)}
.web{position:absolute;left:0;right:0;text-align:center;color:var(--ink);letter-spacing:.12em}

/* Letterhead */
.letterhead{left:183px;top:56px;width:390px;height:555px}
.letterhead .band-top{position:absolute;left:0;top:14px;width:26px;height:170px;background:var(--maroon)}
.letterhead .band-mid{position:absolute;left:0;top:184px;width:12px;height:210px;background:var(--grey)}
.letterhead .band-bottom{position:absolute;left:0;top:394px;width:26px;height:150px;background:var(--maroon)}
.letterhead .logo{position:absolute;left:66px;top:34px;display:flex;align-items:center;gap:6px}
.letterhead .logo .mark{width:16px;height:16px}
.letterhead .logo .brand{font-size:10px}
.contact-list{position:absolute;left:268px;top:24px;list-style:none}
.contact-list li{display:flex;align-items:center;gap:6px;font-size:6px;color:var(--muted);height:17px}
.contact-list svg{width:12px;height:12px;flex:none}
.letter-body{position:absolute;left:58px;top:130px;width:290px;font-size:6px;line-height:9px;color:#58585b}
.letter-body p{margin-bottom:9px}
.signature{width:40px;height:16px;background:#d9d9dc;margin:4px 0 6px;border-radius:2px}
.letterhead .web{bottom:14px;font-size:8px}

/* Folder */
.folder{left:634px;top:36px;width:482px;height:580px}
.folder .band{position:absolute;left:0;top:0;width:46px;height:100%;background:var(--grey)}
.folder .band-top{position:absolute;left:0;top:0;width:26px;height:170px;background:var(--maroon)}
.folder .band-bottom{position:absolute;left:0;bottom:0;width:26px;height:150px;background:var(--maroon)}
.folder .logo{position:absolute;left:46px;right:0;top:255px;display:flex;flex-direction:column;align-items:center;gap:14px}
.folder .logo .mark{width:62px;height:62px}
.folder .logo .brand{font-size:19px}
.folder .web{left:46px;bottom:18px;font-size:11px}

/* Business cards */
.card{left:46px;width:177px;height:107px}
.card-front{top:657px}
.card-back{top:781px}
.card .stripe{position:absolute;left:0;top:0;height:14px;background:var(--maroon)}
.card .stripe-grey{position:absolute;left:0;top:0;height:14px;background:var(--grey)}
.card-front .logo{position:absolute;left:12px;top:36px;display:flex;flex-direction:column;align-items:flex-start;gap:4px}
.card-front .logo .mark{width:14px;height:14px}
.card-front .logo .brand{font-size:6px}
.card-front .person{position:absolute;left:12px;top:72px;font-size:5.5px;line-height:8px}
.card-front .person strong{font-weight:600;color:var(--maroon)}
.card-front .contact-list{left:96px;top:26px}
.card-front .contact-list li{height:14px;font-size:4.6px}
.card-front .contact-list svg{width:9px;height:9px}
.card-back .logo{position:absolute;left:0;right:0;top:38px;display:flex;flex-direction:column;align-items:center;gap:5px}
.card-back .logo .mark{width:16px;height:16px}
.card-back .logo .brand{font-size:7px}

/* Envelopes */
.envelope-front{left:266px;top:667px;width:361px;height:221px}
.envelope-front .band{position:absolute;left:0;top:0;width:8px;height:100%;background:var(--grey)}
.envelope-front .logo{position:absolute;left:34px;top:32px;display:flex;flex-direction:column;align-items:flex-start;gap:8px}
.envelope-front .logo .mark{width:30px;height:30px}
.envelope-front .logo .brand{font-size:10px}
.envelope-front .address{position:absolute;left:34px;top:100px;font-size:6px;color:#58585b}
.envelope-front .web{bottom:46px;font-size:8px}
.envelope-back{left:736px;top:667px;width:418px;height:221px}
.envelope-back svg.flap{position:absolute;left:0;top:0}
.envelope-back .web{top:34px;color:#fff;font-size:13px;letter-spacing:.14em}
</style>
</head>
<body>

<!-- Letterhead -->
<section class="sheet letterhead">
  <div class="band-top"></div>
  <div class="band-mid"></div>
  <div class="band-bottom"></div>
  <div class="logo"><span class="mark"></span><span class="brand">Dorian Valesko, LLP</span></div>
  <ul class="contact-list">
    <li><svg viewBox="0 0 12 12"><circle cx="6" cy="6" r="6" fill="#3a3a3c"/><path d="M4 3.2l1 1.4-.6.8c.4.8 1 1.4 1.8 1.8l.8-.6 1.4 1-.5 1.1C5.8 8.6 3.4 6.2 3.2 4z" fill="#fff"/></svg>(718) 555-0142</li>
    <li><svg viewBox="0 0 12 12"><circle cx="6" cy="6" r="6" fill="#3a3a3c"/><path d="M4 3.2l1 1.4-.6.8c.4.8 1 1.4 1.8 1.8l.8-.6 1.4 1-.5 1.1C5.8 8.6 3.4 6.2 3.2 4z" fill="#fff"/></svg>(718) 555-0198</li>
    <li><svg viewBox="0 0 12 12"><circle cx="6" cy="6" r="6" fill="#3a3a3c"/><rect x="3" y="4" width="6" height="4.2" fill="none" stroke="#fff" stroke-width=".7"/><path d="M3 4l3 2.2L9 4" fill="none" stroke="#fff" stroke-width=".7"/></svg>dorian@valeskolegal.com</li>
    <li><svg viewBox="0 0 12 12"><circle cx="6" cy="6" r="6" fill="#3a3a3c"/><circle cx="6" cy="6" r="2.8" fill="none" stroke="#fff" stroke-width=".7"/><path d="M3.2 6h5.6M6 3.2v5.6" stroke="#fff" stroke-width=".6"/></svg>www.ValeskoLegal.com</li>
  </ul>
  <div class="letter-body">
    <p>June 12, 2024<br>Client Name<br>Harbor Street, Brooklyn NY</p>
    <p>Thank you for choosing our firm to represent your interests. We have reviewed the documents you provided and prepared a summary of the next steps in your matter. Our team will contact you to arrange a meeting at a time that suits your schedule.</p>
    <p>Please bring any contracts, letters and notes related to the case. These records help us give clear advice and protect your position.</p>
    <p>Should you have questions before we meet, do not hesitate to call our office. We look forward to working with you and reaching a good result in this matter together.</p>
    <p>Best Regards,</p>
    <div class="signature" role="img" aria-label="Handwritten signature"></div>
    <p>Dorian Valesko<br>Managing Partner</p>
  </div>
  <div class="web">www.valeskolegal.com</div>
</section>

<!-- Presentation folder -->
<section class="sheet folder">
  <div class="band"></div>
  <div class="band-top"></div>
  <div class="band-bottom"></div>
  <div class="logo"><span class="mark"></span><span class="brand">Dorian Valesko, LLP</span></div>
  <div class="web">www.valeskolegal.com</div>
</section>

<!-- Business card, front -->
<section class="sheet card card-front">
  <div class="stripe-grey" style="width:100%"></div>
  <div class="stripe" style="width:70%"></div>
  <div class="logo"><span class="mark"></span><span class="brand">Dorian Valesko, LLP</span></div>
  <div class="person"><strong>Dorian Valesko</strong><br>Managing Partner</div>
  <ul class="contact-list">
    <li><svg viewBox="0 0 12 12"><circle cx="6" cy="6" r="6" fill="#3a3a3c"/><path d="M4 3.2l1 1.4-.6.8c.4.8 1 1.4 1.8 1.8l.8-.6 1.4 1-.5 1.1C5.8 8.6 3.4 6.2 3.2 4z" fill="#fff"/></svg>(718) 555-0142</li>
    <li><svg viewBox="0 0 12 12"><circle cx="6" cy="6" r="6" fill="#3a3a3c"/><path d="M4 3.2l1 1.4-.6.8c.4.8 1 1.4 1.8 1.8l.8-.6 1.4 1-.5 1.1C5.8 8.6 3.4 6.2 3.2 4z" fill="#fff"/></svg>(718) 555-0198</li>
    <li><svg viewBox="0 0 12 12"><circle cx="6" cy="6" r="6" fill="#3a3a3c"/><rect x="3" y="4" width="6" height="4.2" fill="none" stroke="#fff" stroke-width=".7"/><path d="M3 4l3 2.2L9 4" fill="none" stroke="#fff" stroke-width=".7"/></svg>dorian@valeskolegal.com</li>
    <li><svg viewBox="0 0 12 12"><circle cx="6" cy="6" r="6" fill="#3a3a3c"/><circle cx="6" cy="6" r="2.8" fill="none" stroke="#fff" stroke-width=".7"/><path d="M3.2 6h5.6M6 3.2v5.6" stroke="#fff" stroke-width=".6"/></svg>www.ValeskoLegal.com</li>
    <li><svg viewBox="0 0 12 12"><circle cx="6" cy="6" r="6" fill="#3a3a3c"/><path d="M6 2.8a2.2 2.2 0 0 0-2.2 2.2C3.8 6.8 6 9.2 6 9.2S8.2 6.8 8.2 5A2.2 2.2 0 0 0 6 2.8z" fill="#fff"/></svg>4382 Linden Terrace</li>
  </ul>
</section>

<!-- Business card, back -->
<section class="sheet card card-back">
  <div class="stripe-grey" style="width:100%"></div>
  <div class="stripe" style="width:55%"></div>
  <div class="logo"><span class="mark"></span><span class="brand">Dorian Valesko, LLP</span></div>
</section>

<!-- Envelope, front -->
<section class="sheet envelope-front">
  <div class="logo"><span class="mark"></span><span class="brand">Dorian Valesko, LLP</span></div>
  <div class="address">4382 Linden Terrace Brooklyn, New York 11356</div>
  <div class="web">www.valeskolegal.com</div>
</section>

<!-- Envelope, back -->
<section class="sheet envelope-back">
  <svg class="flap" width="418" height="221" viewBox="0 0 418 221">
    <path d="M0 0H418V78C418 92 410 98 396 98H22C8 98 0 92 0 78Z" fill="var(--maroon)"/>
  </svg>
  <div class="web">www.valeskolegal.com</div>
</section>

</body>
</html>
```